FOOD DELIVERY BRAND NEEDS WEBSITE TO GET SUBSCRIBERS

web design needed for a food delivery brand/label,
website should display who we are, how it works and push futur clients to get the label for an online application. Should look serious/official, trustworthy and confident. colors are black and gold like logo

Target Market(s)

restaurants

Industry/Entity Type

restaurant

Number of Pages Required

4 page

Requirements
Must have
• home page, who we are, our partners, subscribe, 2 subscribe button : 1 on top 1 bottom
Nice to have
• a graphic showing average + 15% sales thanks the label

```html
<!DOCTYPE html>
<html lang="en">
<head>
<meta charset="utf-8">
<title>Gilded Plate Seal</title>
<link href="https://fonts.googleapis.com/css2?family=Roboto:wght@400;500;700;900&display=swap" rel="stylesheet">
<style>
:root{
  --ink:#0c0c0c;
  --ink-soft:#1a1a1a;
  --gold:#f3d690;
  --gold-light:#f8e3a2;
  --gold-deep:#e2bb68;
  --gold-line:#d9b45a;
  --olive:#8a6d1c;
  --white:#ffffff;
  --hero-a:#2b2b2b;
  --hero-b:#5a5a5c;
}
*{margin:0;padding:0;box-sizing:border-box}
html,body{width:1200px;height:3450px;overflow:hidden}
body{position:relative;background:var(--ink);font-family:'Roboto',Arial,sans-serif;color:var(--ink)}
.abs{position:absolute}
.backdrop{position:absolute;left:0;top:0}
.btn{position:absolute;display:flex;align-items:center;justify-content:center;border-radius:5px;font-weight:700;letter-spacing:.5px;text-transform:uppercase}
.btn-gold{background:var(--gold);color:var(--ink)}
.btn-dark{background:var(--ink);color:var(--gold)}

/* header */
.site-header{left:0;top:0;width:1200px;height:111px;border-bottom:1.5px solid var(--gold-line)}
.brand{position:absolute;display:flex;flex-direction:column;align-items:center;font-weight:500;color:var(--gold);text-transform:uppercase;line-height:1.1}
.brand-dot{border-radius:50%;background:var(--gold);margin-bottom:6px}
.brand-header{left:171px;top:14px;width:120px;font-size:13px}
.brand-header .brand-dot{width:36px;height:36px}
.brand-header small{font-size:10px;letter-spacing:1px}
.nav-top{position:absolute;top:72px;left:597px;display:flex;gap:0;font-size:14.5px;font-weight:700;color:var(--white)}
.nav-top span{position:absolute;white-space:nowrap}

/* hero */
.hero-title{left:171px;top:262px;color:var(--gold);font-weight:700;letter-spacing:1px}
.hero-title .l1{display:block;font-size:51px;line-height:60px}
.hero-title .l2{display:block;font-size:43px;line-height:60px;margin-top:8px}
.hero-photo{left:540px;top:235px;width:630px;height:430px;border-radius:40px;background:linear-gradient(135deg,#1c1c1c 0%,#3a3a3c 45%,#0e0e0e 70%,#555 100%);transform:rotate(-4deg)}

/* who */
.who-back{left:162px;top:832px;width:380px;height:505px;background:#b89b55;transform:rotate(-1.2deg)}
.who-photo{left:174px;top:841px;width:367px;height:501px;border:3px solid var(--olive);background:linear-gradient(160deg,#7a7f72 0%,#e9e7e1 40%,#c79a6a 70%,#f2f0ec 100%)}
.section-title{position:absolute;font-weight:700;font-size:32px;letter-spacing:.5px;text-transform:uppercase}
.who-title{left:585px;top:890px}
.who-text{left:585px;top:955px;width:443px;font-size:14.5px;line-height:22.5px;text-align:justify}

/* how */
.how-title{left:0;width:1200px;top:1443px;text-align:center;color:var(--gold)}
.step-label{position:absolute;width:260px;text-align:center;color:var(--gold);font-size:21px;font-weight:700;text-transform:uppercase}
.step-text{position:absolute;width:240px;text-align:center;color:var(--white);font-size:11.5px;line-height:19.5px}

/* partners */
.partners-title{left:0;width:1200px;top:2058px;text-align:center;color:var(--ink-soft)}
.partners-text{left:171px;width:858px;top:2108px;text-align:center;font-size:14.5px;line-height:22px;color:var(--ink-soft)}
.partner{position:absolute;top:2219px;width:200px;height:90px;background:var(--white);border:2px solid var(--ink);border-radius:5px;display:flex;align-items:center;justify-content:center}
.partner i{display:block;width:34px;height:34px;border-radius:50%;background:#cfcfcf}

/* subscribe */
.sub-frame{left:174px;top:2573px;width:852px;height:344px;border:2.5px dotted var(--gold)}
.sub-title{left:493px;top:2538px;width:214px;height:68px;background:var(--gold);display:flex;align-items:center;justify-content:center;font-size:32px;font-weight:700}
.sub-text{left:190px;width:820px;top:2645px;text-align:center;color:var(--white);font-size:16.5px;line-height:30px}

/* footer */
.brand-footer{left:500px;top:3128px;width:200px;font-size:17px;color:var(--ink)}
.brand-footer .brand-dot{width:58px;height:58px;background:var(--ink);margin-bottom:8px}
.brand-footer small{font-size:13px;letter-spacing:1px}
.nav-foot{left:0;width:1200px;top:3288px;display:flex;justify-content:center;gap:22px;font-size:17px;font-weight:700;color:var(--ink)}
.foot-line{left:174px;top:3360px;width:852px;height:1.5px;background:var(--ink)}
.copyright{left:0;width:1200px;top:3396px;text-align:center;font-size:13px}
</style>
</head>
<body>

<svg class="backdrop" width="1200" height="3450" viewBox="0 0 1200 3450" aria-hidden="true">
  <defs>
    <linearGradient id="heroBg" x1="0" y1="0" x2="1" y2="0.3">
      <stop offset="0" stop-color="var(--hero-a)"/>
      <stop offset="0.6" stop-color="#444446"/>
      <stop offset="1" stop-color="var(--hero-b)"/>
    </linearGradient>
    <linearGradient id="goldBg" x1="0" y1="1" x2="1" y2="0">
      <stop offset="0" stop-color="var(--gold-light)"/>
      <stop offset="0.55" stop-color="var(--gold)"/>
      <stop offset="1" stop-color="var(--gold-deep)"/>
    </linearGradient>
    <linearGradient id="shopBg" x1="0" y1="0" x2="1" y2="1">
      <stop offset="0" stop-color="#0a0a0a"/>
      <stop offset="0.5" stop-color="#15130e"/>
      <stop offset="1" stop-color="#0b0b0b"/>
    </linearGradient>
  </defs>
  <rect x="0" y="0" width="1200" height="111" fill="var(--ink)"/>
  <rect x="0" y="111" width="1200" height="700" fill="url(#heroBg)"/>
  <polygon points="0,784 1200,710 1200,1273 0,1199" fill="url(#goldBg)"/>
  <polygon points="0,1199 1200,1273 1200,2025 0,1953" fill="var(--ink)"/>
  <polygon points="0,1953 1200,2025 1200,2381 0,2456" fill="url(#goldBg)"/>
  <polygon points="0,2456 1200,2381 1200,2999 0,3075" fill="url(#shopBg)"/>
  <polygon points="0,3075 1200,2999 1200,3450 0,3450" fill="url(#goldBg)"/>
</svg>
<div class="abs" style="left:0;top:2381px;width:1200px;height:694px" role="img" aria-label="Dimmed photo of a restaurant window covered in delivery service stickers"></div>

<header class="abs site-header">
  <div class="brand brand-header"><span class="brand-dot"></span>Gilded Plate<small>Seal</small></div>
  <div class="btn btn-gold" style="left:927px;top:17px;width:100px;height:38px;font-size:14px">Subscribe</div>
  <nav class="nav-top">
    <span style="left:0">HOME</span>
    <span style="left:75px">WHO WE ARE</span>
    <span style="left:200px">OUR PARTNERS</span>
    <span style="left:346px">SUBSCRIBE</span>
  </nav>
</header>

<section>
  <h1 class="abs hero-title"><span class="l1">GILDED PLATE</span><span class="l2">SEAL</span></h1>
  <div class="btn btn-gold" style="left:171px;top:425px;width:132px;height:48px;font-size:17px">Read more</div>
  <svg class="abs" style="left:171px;top:529px" width="108" height="76" viewBox="0 0 108 76" aria-hidden="true">
    <polyline points="38,2 2,38 38,74" fill="none" stroke="var(--gold)" stroke-width="2"/>
    <polyline points="70,2 106,38 70,74" fill="none" stroke="var(--gold)" stroke-width="2"/>
  </svg>
  <div class="abs hero-photo" role="img" aria-label="Black meal tray with a sealed sleeve holding a burger patty"></div>
</section>

<section>
  <div class="abs who-back"></div>
  <div class="abs who-photo" role="img" aria-label="Courier holding paper bags, coffee cups and a delivery box"></div>
  <h2 class="section-title who-title">Who we are</h2>
  <p class="abs who-text">Sed ut perspiciatis unde omnis iste natus error sit voluptatem accu santium doloremque laudantium, totam rem aperiam, eaque ipsa quae ab illo inventore veritatis et quasi architecto beatae vitae dicta sunt explicabo.</p>
  <div class="btn btn-dark" style="left:585px;top:1082px;width:120px;height:45px;font-size:16px">Read more</div>
</section>

<section>
  <h2 class="section-title how-title">How it works</h2>
  <svg class="abs" style="left:0;top:1500px" width="1200" height="420" viewBox="0 1500 1200 420" aria-hidden="true">
    <g fill="none" stroke="var(--gold)" stroke-width="2.5" stroke-dasharray="2 5" stroke-linecap="round">
      <path d="M126,1684 A163,163 0 0 1 443,1660"/>
      <path d="M443,1680 Q450,1790 520,1815"/>
      <path d="M680,1815 Q750,1790 768,1680"/>
      <path d="M768,1660 A163,163 0 0 1 1085,1684"/>
    </g>
    <circle cx="126" cy="1684" r="6" fill="var(--gold)"/>
    <circle cx="1085" cy="1684" r="6" fill="var(--gold)"/>
    <polygon points="434,1660 452,1660 443,1676" fill="var(--gold)"/>
    <polygon points="759,1676 777,1676 768,1660" fill="var(--gold)"/>

    <circle cx="277" cy="1667" r="85" fill="none" stroke="var(--gold)" stroke-width="3"/>
    <circle cx="922" cy="1667" r="85" fill="none" stroke="var(--gold)" stroke-width="3"/>
    <circle cx="600" cy="1816" r="86" fill="var(--gold)"/>

    <!-- tag icon -->
    <g transform="translate(277 1677) rotate(-45)" fill="none" stroke="var(--gold)" stroke-width="4" stroke-linejoin="round">
      <path d="M-30,-16 L14,-16 L34,0 L14,16 L-30,16 Z"/>
      <circle cx="14" cy="0" r="5"/>
    </g>
    <!-- bowl icon -->
    <g fill="none" stroke="var(--ink)" stroke-width="5" stroke-linecap="round" stroke-linejoin="round">
      <path d="M560,1826 L640,1826"/>
      <path d="M568,1826 Q572,1856 600,1856 Q628,1856 632,1826"/>
      <path d="M586,1812 q-6,-8 0,-16 q6,-8 0,-14"/>
      <path d="M600,1812 q-6,-8 0,-16 q6,-8 0,-14"/>
      <path d="M614,1812 q-6,-8 0,-16 q6,-8 0,-14"/>
    </g>
    <!-- hand with box icon -->
    <g fill="none" stroke="var(--gold)" stroke-width="4" stroke-linejoin="round" stroke-linecap="round">
      <rect x="910" y="1646" width="34" height="30"/>
      <path d="M922,1646 L922,1658 L932,1658 L932,1646"/>
      <path d="M883,1704 L883,1684 L900,1684 Q912,1684 916,1690 L932,1690 Q936,1696 930,1700 L912,1700"/>
      <path d="M883,1704 L930,1704 L958,1688 Q964,1694 958,1700 L938,1712 L883,1712"/>
    </g>

    <g font-family="Roboto, Arial, sans-serif" font-weight="900" font-size="38" text-anchor="middle">
      <circle cx="331" cy="1606" r="36" fill="var(--gold)" stroke="var(--ink)" stroke-width="4"/>
      <text x="331" y="1620" fill="var(--ink)">01</text>
      <circle cx="655" cy="1755" r="36" fill="var(--ink)" stroke="var(--gold)" stroke-width="3"/>
      <text x="655" y="1769" fill="var(--gold)">02</text>
      <circle cx="977" cy="1606" r="36" fill="var(--gold)" stroke="var(--ink)" stroke-width="4"/>
      <text x="977" y="1620" fill="var(--ink)">03</text>
    </g>
  </svg>
  <p class="step-text" style="left:480px;top:1587px">Sed ut perspiciatis unde omnis iste natus error sit voluptatem accusantium dolorem que laudantium</p>
  <div class="step-label" style="left:470px;top:1671px">Nemo enim</div>
  <div class="step-label" style="left:147px;top:1777px">Nemo enim</div>
  <p class="step-text" style="left:157px;top:1819px">Sed ut perspiciatis unde omnis iste natus error sit voluptatem accusantium dolorem que laudantium</p>
  <div class="step-label" style="left:792px;top:1777px">Nemo enim</div>
  <p class="step-text" style="left:802px;top:1819px">Sed ut perspiciatis unde omnis iste natus error sit voluptatem accusantium dolorem que laudantium</p>
</section>

<section>
  <h2 class="section-title partners-title">Our partners</h2>
  <p class="abs partners-text">Sed ut perspiciatis unde omnis iste natus error sit voluptatem accu santium doloremque laudantium, totam rem aperiam, eaque ipsa quae ab illo inventore veritatis</p>
  <div class="partner" style="left:173px"><i></i></div>
  <div class="partner" style="left:390px"><i></i></div>
  <div class="partner" style="left:608px"><i></i></div>
  <div class="partner" style="left:825px"><i></i></div>
</section>

<section>
  <div class="abs sub-frame"></div>
  <h2 class="abs sub-title">SUBSCRIBE</h2>
  <p class="abs sub-text">Nam libero tempore, cum soluta nobis est eligendi optio cumque nihil impedit quo minus id quod maxime placeat facere possimus, omnis voluptas assumenda est, omnis dolor repellendus. Temporibus autem quibus dam et aut officiis debitis aut rerum necessitatibus saepe eveniet ut et voluptates repudiandae sint et molesti ae non recusandae. Itaque earum rerum hic tenetur a sapiente delectus, ut aut reiciendis voluptatibus maiores alias consequatur aut perferendis doloribus asperiores repellat.</p>
  <div class="btn btn-gold" style="left:464px;top:2826px;width:272px;height:47px;font-size:17px">Apply for subscription</div>
</section>

<footer>
  <div class="brand brand-footer"><span class="brand-dot"></span>Gilded Plate<small>Seal</small></div>
  <nav class="abs nav-foot">
    <span>HOME</span><span>|</span><span>WHO WE ARE</span><span>|</span><span>OUR PARTNERS</span><span>|</span><span>SUBSCRIBE</span>
  </nav>
  <div class="abs foot-line"></div>
  <p class="abs copyright">Copyrights @ 2022 Gilded Plate Seal</p>
</footer>

</body>
</html>
```